Alliance of Northern Urgent Care Scholars Poster Design

We need a pull up banner (specs attached) for the Alliance of Northern Urgent Care Scholars. This group enables emergency care researchers to conduct multi-center research or education studies, provide mentorship, create knowledge through research, support knowledge translation, and ultimately improve emergency patient care for all Canadians.

Font styles to use
Serif
Sans Serif

Colors

Designer to choose colors to be used in the design.

Requirements
Must have
• ANUS Logo
• BRTL Logo
• www.brtl.ca
• For more information contact: mdellow@brtl.ca
• Complimentary colours to the ANUS logo.
Nice to have
• Photos of the group (attached to brief) - our photos assuming they are the right resolution. Stock photos can potentially be used if these don't work.
Should not have
• No stock photos containing laboratory equipment.

```html
<!DOCTYPE html>
<html lang="en">
<head>
<meta charset="utf-8">
<title>Alliance of Northern Urgent Care Scholars – Pull Up Banner</title>
<link rel="stylesheet" href="https://fonts.googleapis.com/css2?family=Lato:wght@700;900&family=Montserrat:wght@500;600&display=swap">
<style>
  :root {
    --page-bg: #e4e6ea;
    --blue: #1b6db4;
    --blue-deep: #0e559e;
    --red: #c81b30;
    --mist: #e9eaed;
    --white: #ffffff;
    --ink-grey: #4a4f57;
    --frame: #f4f4f4;
  }
  * { margin: 0; padding: 0; box-sizing: border-box; }
  html, body {
    width: 768px; height: 1200px; overflow: hidden;
    background: var(--page-bg);
  }
  .stage { position: relative; width: 768px; height: 1200px; overflow: hidden; }
  .banner {
    position: absolute; left: 123.5px; top: 0;
    width: 454px; height: 1046px;
    transform: scale(1.1472); transform-origin: top left;
    background: var(--blue); overflow: hidden;
  }
  .banner-shapes { position: absolute; inset: 0; width: 454px; height: 1046px; }

  .headline {
    position: absolute; left: 37px; top: 280px;
    font-family: "Lato", Arial, sans-serif; font-weight: 900;
    font-size: 50px; line-height: 55px; letter-spacing: -0.5px;
    color: var(--white); text-transform: uppercase;
  }

  .photo {
    position: absolute; border: 3px solid var(--frame);
    box-shadow: 2px 3px 6px rgba(0,0,0,0.35);
  }
  .photo-colleagues-outdoors { left: 19px; top: 483px; width: 180px; height: 125px;
    background: linear-gradient(160deg, #5d6b55 0%, #8a8f84 45%, #3c3a3c 100%); }
  .photo-colleagues-dinner { left: 279px; top: 475px; width: 141px; height: 98px;
    background: linear-gradient(170deg, #3a2b24 0%, #6b5047 50%, #c9b8b0 100%); }
  .photo-mountain { left: 159px; top: 583px; width: 260px; height: 182px;
    background: linear-gradient(180deg, #7fb2e3 0%, #a9cbe8 30%, #dfe3e6 48%, #2f4a35 70%, #2a3f2c 100%); }
  .photo-ski-day { left: 32px; top: 701px; width: 200px; height: 140px;
    background: linear-gradient(180deg, #6c5a4c 0%, #cfd2d6 40%, #e4e7ea 60%, #26344e 100%); }

  .logo-row {
    position: absolute; left: 0; top: 858px; width: 454px; height: 100px;
  }
  .partner-logo {
    position: absolute; top: 34px; height: 40px;
    display: flex; align-items: center; gap: 7px;
    font-family: "Lato", Arial, sans-serif; font-weight: 900;
    font-size: 24px; line-height: 1; color: var(--blue);
  }
  .partner-logo::before {
    content: ""; width: 14px; height: 14px; border-radius: 50%;
    background: var(--blue); flex: none;
  }
  .logo-brtl { left: 34px; }
  .logo-anus { left: 140px; }
  .logo-divider {
    position: absolute; left: 249px; top: 14px;
    width: 1.5px; height: 80px; background: var(--ink-grey);
  }
  .network-name {
    position: absolute; left: 264px; top: 22px;
    font-family: "Montserrat", Arial, sans-serif; font-weight: 600;
    font-size: 14px; line-height: 16px;
  }
  .network-name .lead { color: var(--blue); }
  .network-name .rest { color: var(--ink-grey); }

  .contact-band {
    position: absolute; left: 0; top: 963px; width: 454px; height: 83px;
    background: var(--blue); color: var(--white); text-align: center;
    font-family: "Lato", Arial, sans-serif; font-weight: 700;
  }
  .contact-label { margin-top: 9px; font-size: 14.5px; line-height: 18px; }
  .contact-links { margin-top: 2px; font-size: 23px; line-height: 28px; letter-spacing: 0.2px; }
</style>
</head>
<body>
<div class="stage">
  <div class="banner">
    <svg class="banner-shapes" viewBox="0 0 454 1046" aria-hidden="true">
      <polygon points="190,230 454,240 454,560" fill="var(--blue-deep)"/>
      <polygon points="0,178 454,240 454,170" fill="var(--blue-deep)" opacity="0.6"/>
      <polygon points="0,840 262,790 454,905 454,963 0,963" fill="var(--mist)"/>
      <polygon points="454,558 254,783 454,903" fill="var(--red)"/>
    </svg>
    <svg class="banner-shapes" viewBox="0 0 454 1046" role="img" aria-label="Group photo of the research network members gathered in a conference room">
      <defs>
        <linearGradient id="groupTones" x1="0" y1="0" x2="0" y2="1">
          <stop offset="0" stop-color="#d9d2c4"/>
          <stop offset="0.45" stop-color="#8d7f74"/>
          <stop offset="1" stop-color="#2f3138"/>
        </linearGradient>
      </defs>
      <polygon points="0,0 454,0 454,240 0,178" fill="url(#groupTones)"/>
    </svg>

    <h1 class="headline">Northern<br>Urgent Care<br>Scholars</h1>

    <div class="photo photo-colleagues-outdoors" role="img" aria-label="Three colleagues standing together outdoors among trees"></div>
    <div class="photo photo-colleagues-dinner" role="img" aria-label="Three colleagues at an evening event"></div>
    <div class="photo photo-mountain" role="img" aria-label="Snow-capped mountain above an evergreen forest"></div>
    <div class="photo photo-ski-day" role="img" aria-label="Two members in helmets reading a trail map on a ski hill"></div>

    <div class="logo-row">
      <div class="partner-logo logo-brtl">BRTL</div>
      <div class="partner-logo logo-anus">ANUS</div>
      <div class="logo-divider"></div>
      <div class="network-name">
        <div class="lead">Alliance of</div>
        <div class="lead">Northern</div>
        <div class="rest">Urgent Care</div>
        <div class="rest">Scholars</div>
      </div>
    </div>

    <div class="contact-band">
      <p class="contact-label">For more information contact:</p>
      <p class="contact-links">mdellow@brtl.ca | www.brtl.ca</p>
    </div>
  </div>
</div>
</body>
</html>
```